Knee Wraps

brand name is velmo
300g package
collagen product containing bovine collagen peptides
orange packaging color
with turmeric added
ultimate complex for joints flexibility & mobility
ingredients
collagen, turmeric curcumin, vitamin c
a product that takes care of the joints mobility and provides resilience against injuries

similar design to the packaging in the files

Target Market(s)

fitness, health products

Industry/Entity Type

health and fitness

Colors
F0912C
F2A743
F7CA91
FBE8D2
FDF5EE

Requirements
Must have
• very clear message of the advantage of the product which is providing flexible joints, increased mobility, great inflammation response, amazing skin hair bones and nails care
Nice to have
• turmeric design or something that indicates the product containing organic turmeric, orange fresh design, something to makes me feel happy with movement of my body/joints

```html
<!DOCTYPE html>
<html lang="en">
<head>
<meta charset="utf-8">
<title>Velmo Collagen Peptides – Turmeric Label</title>
<link rel="stylesheet" href="https://fonts.googleapis.com/css2?family=Poppins:wght@400;600;700;800&display=swap">
<style>
  :root {
    --orange: #F0912C;
    --orange-light: #F2A743;
    --peach: #F7CA91;
    --cream: #FBE8D2;
    --white: #FFFFFF;
    --backdrop: #E9E9EB;
  }
  * { margin: 0; padding: 0; box-sizing: border-box; }
  html, body { width: 1125px; height: 1200px; overflow: hidden; }
  body {
    background: var(--backdrop);
    font-family: "Poppins", sans-serif;
    position: relative;
  }
  .label {
    position: absolute;
    left: 45px; top: 10px;
    width: 1035px; height: 1180px;
    background: linear-gradient(100deg, var(--orange) 0%, var(--orange) 55%, var(--orange-light) 100%);
    color: var(--white);
    overflow: hidden;
  }
  .brand-banner {
    position: absolute;
    left: 82px; top: 38px;
    width: 873px; height: 157px;
  }
  .brand-name {
    position: absolute;
    left: 82px; top: 38px;
    width: 873px; height: 157px;
    display: flex; align-items: center; justify-content: center;
    font-weight: 800;
    font-size: 110px;
    letter-spacing: 4px;
    color: var(--orange);
    line-height: 1;
    padding-top: 8px;
  }
  .product-title {
    position: absolute;
    left: 0; width: 100%;
    top: 228px;
    text-align: center;
    font-weight: 800;
    font-size: 140px;
    line-height: 1;
    letter-spacing: -1px;
  }
  .product-subtitle {
    position: absolute;
    left: 0; width: 100%;
    top: 385px;
    text-align: center;
    font-weight: 600;
    font-size: 54px;
    line-height: 1;
  }
  .tagline {
    position: absolute;
    left: 0; width: 100%;
    top: 455px;
    text-align: center;
    font-weight: 600;
    font-size: 24px;
    letter-spacing: 1px;
    line-height: 1;
    color: var(--cream);
  }
  .benefits {
    position: absolute;
    left: 240px; top: 505px;
    list-style: none;
  }
  .benefit {
    display: flex; align-items: center;
    gap: 14px;
    font-size: 28px;
    font-weight: 400;
    height: 50px;
  }
  .benefit svg { width: 36px; height: 36px; flex: none; }
  .turmeric-art {
    position: absolute;
    left: 730px; top: 500px;
    width: 320px; height: 460px;
    background: radial-gradient(ellipse at 50% 50%, var(--peach) 0%, rgba(247,202,145,0.35) 55%, rgba(242,167,67,0) 75%);
  }
  .flavour-tag {
    position: absolute;
    left: 250px; top: 735px;
    width: 430px; height: 88px;
    background: var(--white);
    border-radius: 6px;
    display: flex; align-items: center; justify-content: center;
    color: var(--orange);
    font-weight: 700;
    font-size: 50px;
    line-height: 1;
  }
  .ingredients {
    position: absolute;
    left: 245px; top: 842px;
    font-size: 33px;
    font-weight: 400;
    line-height: 1.35;
  }
  .supplement-type {
    position: absolute;
    left: 247px; top: 995px;
    font-size: 46px;
    font-weight: 600;
    line-height: 1;
  }
  .net-weight {
    position: absolute;
    left: 247px; top: 1065px;
    font-size: 36px;
    font-weight: 400;
    line-height: 1;
  }
</style>
</head>
<body>
  <main class="label">
    <svg class="brand-banner" viewBox="0 0 873 157" aria-hidden="true">
      <polygon points="0,0 873,0 790,157 83,157" fill="#FFFFFF"/>
    </svg>
    <div class="brand-name">VELMO</div>

    <h1 class="product-title">COLLAGEN</h1>
    <p class="product-subtitle">PEPTIDES TYPE I &amp; III</p>
    <p class="tagline">ULTIMATE COMPLEX FOR JOINTS FLEXIBILITY &amp; MOBILITY</p>

    <ul class="benefits">
      <li class="benefit">
        <svg viewBox="0 0 38 38" aria-hidden="true">
          <circle cx="19" cy="19" r="16" fill="none" stroke="#fff" stroke-width="2"/>
          <circle cx="19" cy="19" r="5" fill="none" stroke="#fff" stroke-width="2"/>
        </svg>
        skin, hair, bones and nails care
      </li>
      <li class="benefit">
        <svg viewBox="0 0 38 38" aria-hidden="true">
          <circle cx="19" cy="19" r="16" fill="none" stroke="#fff" stroke-width="2"/>
          <circle cx="21" cy="10" r="2.5" fill="#fff"/>
          <path d="M14 28 L19 20 L24 24 M19 20 L20 14 L26 17 M20 14 L13 17" fill="none" stroke="#fff" stroke-width="2" stroke-linecap="round"/>
        </svg>
        increased mobility
      </li>
      <li class="benefit">
        <svg viewBox="0 0 38 38" aria-hidden="true">
          <circle cx="19" cy="19" r="16" fill="none" stroke="#fff" stroke-width="2"/>
          <path d="M13 10 L17 19 L15 29 M23 10 L21 19 L24 29" fill="none" stroke="#fff" stroke-width="2" stroke-linecap="round"/>
        </svg>
        providing flexible joints
      </li>
      <li class="benefit">
        <svg viewBox="0 0 38 38" aria-hidden="true">
          <circle cx="19" cy="19" r="16" fill="none" stroke="#fff" stroke-width="2"/>
          <path d="M19 10 C23 16 25 19 25 22 A6 6 0 0 1 13 22 C13 19 15 16 19 10 Z" fill="none" stroke="#fff" stroke-width="2" stroke-linejoin="round"/>
        </svg>
        great inflammation response
      </li>
    </ul>

    <div class="turmeric-art" role="img" aria-label="Line drawing of a turmeric root"></div>

    <div class="flavour-tag">TURMERIC</div>

    <p class="ingredients">Ingredients: Collagen,<br>Turmeric Curcumin, Vitamin C</p>

    <p class="supplement-type">DIETARY SUPPLEMENT</p>
    <p class="net-weight">NET WT 11OZ (300 G)</p>
  </main>
</body>
</html>
```